Menu revision for Korean Restaurant

I have posted the exact content in a word file that I would like to appear in the menu. Please apply to the template. I will be following up with prices shortly. I am in a hurry and not too picky. Thank you.

Make a menu with revisions.

Page 1: Cover Page
- Replace logo with new uploaded logo

Page 2:
Appetizers
Vegetarian Appetizers

Page 3:
BBQ Items

Page 4:
Signature Dishes

Page 5:
Bokkeum | Stir-Fry

Page 6:
Rice Bowls
Noodles
Hot Soup

Page 7:
Drinks

Target Market(s)

My customers

Industry/Entity Type

Restaurant

Requirements
Must have
• 1. Only use my menu content, template, and font.

```html
<!DOCTYPE html>
<html lang="en">
<head>
<meta charset="utf-8">
<title>Appetizers Menu</title>
<link href="https://fonts.googleapis.com/css2?family=Barlow:wght@700;800&family=Crimson+Text:wght@400;700&family=Nanum+Myeongjo:wght@400;700&display=swap" rel="stylesheet">
<style>
  :root{
    --bg:#111416;
    --gold:#c9b25a;
    --frame:#8f7f3f;
    --text:#e6e1d3;
    --red:#b3141d;
    --veg:#3fdc1c;
    --ornament:#3b3521;
  }
  html,body{margin:0;padding:0;width:927px;height:1200px;overflow:hidden;background:var(--bg);}
  .menu{position:relative;width:1159px;height:1500px;transform:scale(0.8);transform-origin:0 0;background:var(--bg);color:var(--text);font-family:"Crimson Text",Georgia,serif;}
  .frame{position:absolute;inset:0;}
  .title{position:absolute;top:62px;left:0;width:1159px;text-align:center;margin:0;font-family:"Barlow",Arial,sans-serif;font-weight:800;font-size:64px;letter-spacing:10px;color:var(--red);line-height:1;}
  .item{position:absolute;width:485px;margin:0;font-size:19.5px;line-height:27px;letter-spacing:0.6px;text-align:justify;}
  .item .name{font-family:"Barlow",Arial,sans-serif;font-weight:700;font-size:18px;letter-spacing:1.6px;color:var(--gold);}
  .item .ko{font-family:"Nanum Myeongjo",serif;color:var(--gold);font-size:17px;letter-spacing:2px;}
  .item .price{font-weight:700;font-size:17px;letter-spacing:1px;}
  .left{left:68px;}
  .right{left:602px;}
  .veg{position:absolute;width:22px;height:22px;}
  .note{position:absolute;top:1434px;left:99px;font-size:15.5px;letter-spacing:0.6px;margin:0;}
  .note-legend{position:absolute;top:1434px;left:434px;display:flex;align-items:center;gap:8px;font-size:15.5px;letter-spacing:0.6px;}
  .note-legend svg{width:22px;height:22px;}
</style>
</head>
<body>
<div class="menu">
  <svg class="frame" width="1159" height="1500" viewBox="0 0 1159 1500" aria-hidden="true">
    <g fill="none" stroke="var(--frame)" stroke-width="2">
      <path d="M83 20H1073V80H1133V1418H1073V1478H83V1418H24V80H83Z"/>
      <rect x="47" y="44" width="24" height="24"/>
      <rect x="1086" y="44" width="24" height="24"/>
      <rect x="47" y="1430" width="24" height="24"/>
      <rect x="1086" y="1430" width="24" height="24"/>
    </g>
    <g stroke="var(--frame)" stroke-width="1.5">
      <line x1="68" y1="294" x2="265" y2="294"/><line x1="361" y1="294" x2="553" y2="294"/>
      <line x1="68" y1="482" x2="265" y2="482"/><line x1="361" y1="482" x2="553" y2="482"/>
      <line x1="68" y1="649" x2="265" y2="649"/><line x1="361" y1="649" x2="553" y2="649"/>
      <line x1="68" y1="822" x2="265" y2="822"/><line x1="361" y1="822" x2="553" y2="822"/>
      <line x1="68" y1="1020" x2="265" y2="1020"/><line x1="361" y1="1020" x2="553" y2="1020"/>
      <line x1="68" y1="1202" x2="265" y2="1202"/><line x1="361" y1="1202" x2="553" y2="1202"/>
      <line x1="602" y1="293" x2="800" y2="293"/><line x1="896" y1="293" x2="1087" y2="293"/>
      <line x1="602" y1="481" x2="800" y2="481"/><line x1="896" y1="481" x2="1087" y2="481"/>
      <line x1="602" y1="648" x2="800" y2="648"/><line x1="896" y1="648" x2="1087" y2="648"/>
      <line x1="602" y1="833" x2="800" y2="833"/><line x1="896" y1="833" x2="1087" y2="833"/>
      <line x1="602" y1="982" x2="800" y2="982"/><line x1="896" y1="982" x2="1087" y2="982"/>
      <line x1="602" y1="1125" x2="800" y2="1125"/><line x1="896" y1="1125" x2="1087" y2="1125"/>
      <line x1="602" y1="1284" x2="800" y2="1284"/><line x1="896" y1="1284" x2="1087" y2="1284"/>
    </g>
    <g fill="var(--ornament)" stroke="var(--frame)" stroke-width="1.5">
      <circle cx="315" cy="294" r="29" role="img" aria-label="Round ornamental medallion"/>
      <circle cx="315" cy="482" r="29" role="img" aria-label="Round ornamental medallion"/>
      <circle cx="315" cy="649" r="29" role="img" aria-label="Round ornamental medallion"/>
      <circle cx="315" cy="822" r="29" role="img" aria-label="Round ornamental medallion"/>
      <circle cx="315" cy="1020" r="29" role="img" aria-label="Round ornamental medallion"/>
      <circle cx="315" cy="1202" r="29" role="img" aria-label="Round ornamental medallion"/>
      <circle cx="848" cy="293" r="29" role="img" aria-label="Round ornamental medallion"/>
      <circle cx="848" cy="481" r="29" role="img" aria-label="Round ornamental medallion"/>
      <circle cx="848" cy="648" r="29" role="img" aria-label="Round ornamental medallion"/>
      <circle cx="848" cy="833" r="29" role="img" aria-label="Round ornamental medallion"/>
      <circle cx="848" cy="982" r="29" role="img" aria-label="Round ornamental medallion"/>
      <circle cx="848" cy="1125" r="29" role="img" aria-label="Round ornamental medallion"/>
      <circle cx="848" cy="1284" r="29" role="img" aria-label="Round ornamental medallion"/>
    </g>
    <g>
      <g transform="translate(1076 268)"><circle r="11" fill="var(--veg)"/><text y="6" text-anchor="middle" font-family="Crimson Text, serif" font-style="italic" font-weight="700" font-size="18" fill="#fff">v</text></g>
      <g transform="translate(1076 457)"><circle r="11" fill="var(--veg)"/><text y="6" text-anchor="middle" font-family="Crimson Text, serif" font-style="italic" font-weight="700" font-size="18" fill="#fff">v</text></g>
      <g transform="translate(1076 623)"><circle r="11" fill="var(--veg)"/><text y="6" text-anchor="middle" font-family="Crimson Text, serif" font-style="italic" font-weight="700" font-size="18" fill="#fff">v</text></g>
      <g transform="translate(1076 808)"><circle r="11" fill="var(--veg)"/><text y="6" text-anchor="middle" font-family="Crimson Text, serif" font-style="italic" font-weight="700" font-size="18" fill="#fff">v</text></g>
      <g transform="translate(1076 957)"><circle r="11" fill="var(--veg)"/><text y="6" text-anchor="middle" font-family="Crimson Text, serif" font-style="italic" font-weight="700" font-size="18" fill="#fff">v</text></g>
      <g transform="translate(1076 1099)"><circle r="11" fill="var(--veg)"/><text y="6" text-anchor="middle" font-family="Crimson Text, serif" font-style="italic" font-weight="700" font-size="18" fill="#fff">v</text></g>
      <g transform="translate(1076 1259)"><circle r="11" fill="var(--veg)"/><text y="6" text-anchor="middle" font-family="Crimson Text, serif" font-style="italic" font-weight="700" font-size="18" fill="#fff">v</text></g>
      <g transform="translate(1076 1389)"><circle r="11" fill="var(--veg)"/><text y="6" text-anchor="middle" font-family="Crimson Text, serif" font-style="italic" font-weight="700" font-size="18" fill="#fff">v</text></g>
    </g>
  </svg>

  <h1 class="title">APPETIZERS</h1>

  <p class="item left" style="top:180px"><span class="name">MANDU</span> <span class="ko">군만두</span> Beef pot stickers fried and served with a side of house made soy-dipping sauce. <span class="price">$5.95</span></p>
  <p class="item left" style="top:346px"><span class="name">MUL MANDU</span> <span class="ko">물만두</span> Beef pot stickers boiled and served with a side of house made soy-dipping sauce. <span class="price">$5.95</span></p>
  <p class="item left" style="top:535px"><span class="name">CHICKEN WINGS</span> <span class="ko">닭날개</span> Fried chicken wings served with sweet and sour sauce. <span class="price">$8.95</span></p>
  <p class="item left" style="top:704px"><span class="name">SPICY WINGS</span> <span class="ko">닭날개</span> Fried and drizzled in Garam’s original wing sauce. <span class="price">$8.95</span></p>
  <p class="item left" style="top:883px"><span class="name">SHRIMP TEMPURA</span> <span class="ko">새우튀김</span> Jumbo shrimp fried in a crispy tempura batter with an assortment of fried onion, zucchini, and mushroom. <span class="price">$15.95</span></p>
  <p class="item left" style="top:1079px"><span class="name">FRIED CALAMARI</span> <span class="ko">오징어튀김</span> Calamari fried in a light batter.<br><span class="price">$13.95</span></p>
  <p class="item left" style="top:1265px"><span class="name">HAEMUL PAJEON</span> <span class="ko">해물파전</span> Fresh calamari, shrimp, scallops, mussels, and scallions in a Korean pancake. <span class="price">$15.95</span></p>

  <p class="item right" style="top:180px"><span class="name">VEGGIE MANDU</span> <span class="ko">야채만두</span> Vegetable pot stickers fried and served with a side of house made soy-dipping sauce. <span class="price">$5.95</span></p>
  <p class="item right" style="top:346px"><span class="name">VEGGIE MUL MANDU</span> <span class="ko">야채물만두</span> Vegetable pot stickers boiled and served with a side of house made soy-dipping sauce. <span class="price">$5.95</span></p>
  <p class="item right" style="top:536px"><span class="name">SWEET POTATO TEMPURA</span> <span class="ko">고구마튀김</span> Crispy sweet potato slices fried in a light tempura batter. <span class="price">$6.95</span></p>
  <p class="item right" style="top:704px"><span class="name">VEGGIE TEMPURA</span> <span class="ko">야채튀김</span> Vegetable medley of julienned carrot, onion, and succhini fried in a crispy tempura batter. <span class="price">$6.95</span></p>
  <p class="item right" style="top:887px"><span class="name">MUSHROOM TEMPURA</span> <span class="ko">버섯튀김</span> Fried button mushrooms. <span class="price">$5.95</span></p>
  <p class="item right" style="top:1040px;width:495px;text-align:left"><span class="name">PAJEON</span> <span class="ko">파전</span> Pan fried green onion pancake. <span class="price">$12.95</span></p>
  <p class="item right" style="top:1184px"><span class="name">HOBAK GOCHU JEON</span> <span class="ko">호박고추전</span> Zucchini and Jalapeño pancake. <span class="price">$12.95</span></p>
  <p class="item right" style="top:1340px"><span class="name">KIMCHI PAJEON</span> <span class="ko">김치파전</span> Crispy kimchi and scallion pancake. <span class="price">$12.95</span></p>

  <p class="note">*Jeon batter contains wheat flour &amp; eggs.</p>
  <div class="note-legend">
    <svg viewBox="-11 -11 22 22" aria-hidden="true"><circle r="11" fill="var(--veg)"/><text y="6" text-anchor="middle" font-family="Crimson Text, serif" font-style="italic" font-weight="700" font-size="18" fill="#fff">v</text></svg>
    <span>Vegetarian</span>
  </div>
</div>
</body>
</html>
```